Small rum distillery looking for bottle design

Small rum distillery in Estonia. Looking for bottle lable design. It should be simple but at the same time point out from the variety of other bottles.
As we are a small nordic country, design can be some how nordic or represent our country. It can also have some connection with sailing or sea as we know it pirates love it.
Bottle we are using is Brisela 500

Industry/Entity Type

food and beverage

Other font styles liked:
• Baskerville

```html
<!DOCTYPE html>
<html lang="en">
<head>
<meta charset="utf-8">
<title>Halvik Distillery — Rum Label</title>
<link rel="stylesheet" href="https://fonts.googleapis.com/css2?family=Libre+Baskerville:wght@400;700&family=Rye&family=Roboto+Condensed:wght@400&display=swap">
<style>
  :root {
    --page: #ffffff;
    --label-black: #0d0b0a;
    --gold: #c89a3e;
    --gold-dark: #5a3c10;
    --amber: #eaa935;
    --amber-light: #f6cf6a;
    --ember: #b6521b;
    --maroon: #4a0f12;
    --maroon-deep: #2a070a;
    --rum-red: #c21f2d;
    --ink-white: #f6f1e8;
  }
  * { box-sizing: border-box; margin: 0; padding: 0; }
  html, body {
    width: 1200px; height: 1200px; overflow: hidden;
    background: var(--page);
  }
  .label {
    position: absolute; left: 143px; top: 86px;
    width: 914px; height: 1027px;
    background: var(--label-black);
    overflow: hidden;
  }
  .ornament-band {
    position: absolute; left: 0; width: 100%; height: 58px;
    background:
      linear-gradient(180deg, var(--label-black) 0%, var(--gold-dark) 22%, var(--gold) 50%, var(--gold-dark) 78%, var(--label-black) 100%);
  }
  .ornament-band--top { top: 4px; }
  .ornament-band--bottom { bottom: 4px; }
  .scene-art {
    position: absolute; left: 14px; top: 78px; width: 886px; height: 812px;
    background:
      linear-gradient(180deg,
        rgba(42,7,10,0) 0%,
        rgba(42,7,10,0) 34%,
        rgba(74,15,18,.78) 46%,
        rgba(74,15,18,.85) 60%,
        rgba(74,15,18,.35) 72%,
        rgba(182,82,27,.15) 80%,
        rgba(42,7,10,.8) 100%),
      radial-gradient(ellipse 60% 42% at 50% 26%, var(--amber-light) 0%, var(--amber) 35%, var(--ember) 72%, var(--maroon) 100%),
      var(--maroon);
  }
  .brand {
    position: absolute; left: 0; top: 92px; width: 100%;
    text-align: center; color: var(--ink-white);
    font-family: "Libre Baskerville", serif;
  }
  .brand__dot {
    width: 54px; height: 54px; margin: 0 auto 24px;
    border-radius: 50%; background: var(--ink-white);
  }
  .brand__name {
    display: inline-block;
    font-size: 56px; line-height: 1; letter-spacing: 2px;
    padding: 0 14px 8px;
    border-bottom: 3px solid var(--ink-white);
  }
  .brand__sub {
    font-size: 19px; letter-spacing: 9px; margin-top: 10px;
  }
  .product-name {
    position: absolute; left: 0; top: 520px; width: 100%;
    font-family: "Rye", serif; font-size: 215px; line-height: 1;
    font-weight: 400;
    color: var(--rum-red); text-align: center;
    text-shadow:
      3px 0 0 var(--ink-white), -3px 0 0 var(--ink-white),
      0 3px 0 var(--ink-white), 0 -3px 0 var(--ink-white),
      2px 2px 0 var(--ink-white), -2px -2px 0 var(--ink-white),
      2px -2px 0 var(--ink-white), -2px 2px 0 var(--ink-white);
  }
  .facts {
    position: absolute; top: 892px; color: var(--ink-white); text-align: center;
  }
  .facts__value { font-family: "Roboto Condensed", sans-serif; font-size: 42px; line-height: 1; }
  .facts__unit { font-family: "Libre Baskerville", serif; font-size: 21px; margin-top: 4px; }
  .facts--volume { left: 66px; }
  .facts--abv { right: 58px; }
  .origin {
    position: absolute; left: 0; top: 932px; width: 100%;
    text-align: center; color: var(--ink-white);
    font-family: "Libre Baskerville", serif; font-size: 19px; letter-spacing: 2.5px;
  }
</style>
</head>
<body>
  <main class="label">
    <div class="ornament-band ornament-band--top" role="img" aria-label="Gold interlaced knotwork and spiral border"></div>
    <div class="scene-art" role="img" aria-label="Illustration of a pirate ship with dark red sails among storm clouds and waves under a glowing amber sky"></div>

    <header class="brand">
      <div class="brand__dot"></div>
      <div class="brand__name">HALVIK</div>
      <div class="brand__sub">DISTILLERY</div>
    </header>

    <h1 class="product-name">RUM</h1>

    <div class="facts facts--volume">
      <div class="facts__value">500</div>
      <div class="facts__unit">ml</div>
    </div>
    <p class="origin">DISTILLERY IN ESTONIA</p>
    <div class="facts facts--abv">
      <div class="facts__value">41%</div>
      <div class="facts__unit">vol alc</div>
    </div>

    <div class="ornament-band ornament-band--bottom" role="img" aria-label="Gold interlaced knotwork and spiral border"></div>
  </main>
</body>
</html>
```